bright frame masters

we are a window and door installation company for residential and commercial buildings

These cards are for Colin Mercer
His email is colin@brightframemastersco.com and he is a project manager.

Are colors are white red and black

I want all of his information on the card and a few pictures of windows and doors

```html
<!DOCTYPE html>
<html lang="en">
<head>
<meta charset="utf-8">
<title>Bright Frame Masters – Business Card</title>
<link href="https://fonts.googleapis.com/css2?family=Libre+Baskerville:wght@700&family=Poppins:wght@400;500&display=swap" rel="stylesheet">
<style>
  :root {
    --brand-red: #a3192f;
    --ink: #1d1d1f;
    --paper: #ffffff;
    --stage: #e9e9ec;
    --serif: "Libre Baskerville", Georgia, serif;
    --sans: "Poppins", Arial, sans-serif;
  }
  * { box-sizing: border-box; margin: 0; padding: 0; }
  html, body { width: 1200px; height: 880px; overflow: hidden; background: var(--stage); }
  .stage {
    width: 1200px; height: 880px;
    display: flex; flex-direction: column; align-items: center; justify-content: center; gap: 24px;
  }
  .card {
    position: relative; width: 700px; height: 400px;
    border-radius: 22px; overflow: hidden;
    box-shadow: 0 6px 20px rgba(0,0,0,.18);
    background: var(--paper);
  }

  /* Front */
  .front-photo {
    position: absolute; inset: 0;
    background:
      linear-gradient(165deg, #8ea3d4 0%, #c9c7d6 22%, #efe9e2 38%, #d8b98e 55%, #6b5847 72%, #2a2320 100%);
  }
  .front-brand {
    position: absolute; left: 330px; top: 238px;
    color: var(--paper); text-align: center; font-family: var(--serif); font-weight: 700;
    transform: rotate(-18deg); transform-origin: center;
    text-shadow: 0 1px 3px rgba(0,0,0,.45);
  }
  .front-brand .name { font-size: 25px; letter-spacing: .5px; text-transform: uppercase; }
  .front-brand .tag { font-size: 11px; letter-spacing: 1px; text-transform: uppercase; margin-top: 2px; }
  .front-brand .phone { font-size: 22px; margin-top: 2px; }

  /* Back */
  .back-art { position: absolute; inset: 0; }
  .contact {
    position: absolute; left: 50px; top: 140px; color: var(--ink); font-family: var(--sans);
  }
  .contact .person { font-family: var(--serif); font-weight: 700; color: var(--brand-red); font-size: 26px; text-transform: uppercase; }
  .contact .role { font-size: 17px; margin-bottom: 6px; }
  .contact .line { display: flex; align-items: center; gap: 10px; font-size: 17px; line-height: 1.45; }
  .contact .icon { width: 20px; height: 20px; flex: none; }

  .brand-block {
    position: absolute; left: 470px; top: 160px; font-family: var(--serif); font-weight: 700; color: var(--brand-red);
  }
  .brand-block .mark { width: 30px; height: 30px; border-radius: 50%; background: var(--brand-red); margin-bottom: 6px; }
  .brand-block .name { font-size: 19px; line-height: 1.1; text-transform: uppercase; }
  .brand-block .tag { font-size: 8.5px; letter-spacing: .5px; text-transform: uppercase; margin-top: 4px; }
  .brand-block .phone { font-size: 18px; margin-top: 1px; }
  .website {
    position: absolute; right: 28px; bottom: 52px; font-family: var(--sans); font-size: 15px; color: var(--ink);
  }
</style>
</head>
<body>
<main class="stage">

  <section class="card card-front">
    <div class="front-photo" role="img" aria-label="Photo of a modern white house at dusk with large lit glass windows"></div>
    <div class="front-brand">
      <p class="name">Bright Frame Masters</p>
      <p class="tag">Residential &amp; Commercial</p>
      <p class="phone">(407) 555-0142</p>
    </div>
  </section>

  <section class="card card-back">
    <svg class="back-art" viewBox="0 0 700 400" width="700" height="400">
      <defs>
        <linearGradient id="windowsTop" x1="0" y1="0" x2="1" y2="1">
          <stop offset="0" stop-color="#a7793f"/>
          <stop offset=".5" stop-color="#7f8f5a"/>
          <stop offset="1" stop-color="#e9dcc2"/>
        </linearGradient>
        <linearGradient id="doorsBottom" x1="0" y1="0" x2="1" y2="1">
          <stop offset="0" stop-color="#c9d6d8"/>
          <stop offset=".55" stop-color="#8fae8e"/>
          <stop offset="1" stop-color="#7a2550"/>
        </linearGradient>
      </defs>
      <g role="img" aria-label="Photo of tall white-framed windows looking out onto trees">
        <path d="M330 0 C380 110 560 140 700 70 L700 0 Z" fill="url(#windowsTop)"/>
      </g>
      <path d="M360 70 C430 145 590 150 700 75 L700 95 C590 170 420 160 360 70 Z" fill="var(--brand-red)"/>
      <g role="img" aria-label="Photo of a glass entrance with sliding doors beside a garden">
        <path d="M0 330 C90 270 300 265 470 400 L0 400 Z" fill="url(#doorsBottom)"/>
      </g>
      <path d="M0 310 C100 255 320 250 490 400 L470 400 C300 265 90 270 0 330 Z" fill="var(--brand-red)"/>
    </svg>

    <div class="contact">
      <p class="person">Colin Mercer</p>
      <p class="role">Project Manager</p>
      <p class="line">
        <svg class="icon" viewBox="0 0 20 20"><circle cx="10" cy="10" r="10" fill="var(--brand-red)"/><path d="M6 7c1-2 7-2 8 0l-1.5 1.5h-5z M7 10h6l1 4H6z" fill="#fff"/></svg>
        407-555-0187
      </p>
      <p class="line">
        <svg class="icon" viewBox="0 0 20 20"><circle cx="10" cy="10" r="10" fill="var(--brand-red)"/><rect x="5" y="6.5" width="10" height="7" fill="#fff"/><path d="M5 6.5l5 4 5-4" fill="none" stroke="var(--brand-red)" stroke-width="1"/></svg>
        colin@brightframemastersco.com
      </p>
    </div>

    <div class="brand-block">
      <div class="mark"></div>
      <p class="name">Bright<br>Frame<br>Masters</p>
      <p class="tag">Residential &amp; Commercial</p>
      <p class="phone">(407) 555-0142</p>
    </div>
    <p class="website">www.brightframemastersco.com</p>
  </section>

</main>
</body>
</html>
```